Brenway Productions photography and video creator

I need a business card for my production company. I shoot photography and videography for real estate, adventure sports and businesses

simple not to busy

Colors

Designer to choose colors to be used in the design.

Requirements
Must have
• dara@brenwayproductions.ca
• phone -5803317264
• instagram dara_brenway

```html
<!DOCTYPE html>
<html lang="en">
<head>
<meta charset="utf-8">
<title>Brenway Productions – Business Card</title>
<link rel="stylesheet" href="https://fonts.googleapis.com/css2?family=Montserrat:wght@400;500;700&display=swap">
<style>
  :root {
    --page-bg: #d9d9d9;
    --card-bg: #f7f7f7;
    --ink: #1c1c1c;
    --ink-soft: #333333;
    --rule: #222222;
  }
  * { margin: 0; padding: 0; box-sizing: border-box; }
  html, body {
    width: 1200px;
    height: 1021px;
    overflow: hidden;
    background: var(--page-bg);
    font-family: "Montserrat", Arial, sans-serif;
    color: var(--ink);
  }
  .canvas {
    width: 1200px;
    height: 1021px;
    display: flex;
    flex-direction: column;
    align-items: center;
    justify-content: center;
    gap: 44px;
  }
  .card {
    position: relative;
    width: 760px;
    height: 434px;
    background: var(--card-bg);
    box-shadow: 0 6px 18px rgba(0,0,0,0.18);
  }

  /* Front */
  .corner {
    position: absolute;
    width: 78px;
    height: 44px;
    border-color: var(--rule);
    border-style: solid;
    border-width: 0;
  }
  .corner--tl { top: 38px; left: 48px; border-top-width: 4px; border-left-width: 4px; }
  .corner--bl { bottom: 38px; left: 48px; border-bottom-width: 4px; border-left-width: 4px; }
  .corner--tr { top: 38px; right: 48px; border-top-width: 4px; border-right-width: 4px; }
  .corner--br { bottom: 38px; right: 48px; border-bottom-width: 4px; border-right-width: 4px; }

  .front-mark {
    position: absolute;
    inset: 0;
    display: flex;
    align-items: center;
    justify-content: center;
    gap: 22px;
  }
  .front-mark__dot {
    width: 74px;
    height: 74px;
    border-radius: 50%;
    background: var(--ink);
  }
  .wordmark {
    font-weight: 700;
    color: var(--ink);
    line-height: 1;
  }
  .wordmark__name { display: block; font-size: 46px; letter-spacing: 1px; }
  .wordmark__sub { display: block; font-size: 13px; letter-spacing: 8.4px; margin-top: 6px; }

  /* Back */
  .back {
    display: flex;
    align-items: center;
  }
  .back__brand {
    width: 360px;
    display: flex;
    justify-content: center;
  }
  .back__divider {
    width: 2px;
    height: 150px;
    background: var(--rule);
  }
  .back__details {
    padding-left: 44px;
  }
  .person__name {
    font-size: 22px;
    font-weight: 700;
    letter-spacing: 0.5px;
  }
  .person__role {
    font-size: 17px;
    font-weight: 400;
    color: var(--ink-soft);
    margin-bottom: 18px;
  }
  .contact {
    list-style: none;
    font-size: 18px;
    color: var(--ink-soft);
  }
  .contact__item {
    display: flex;
    align-items: center;
    gap: 8px;
    line-height: 1.35;
  }
  .contact__icon { width: 16px; height: 16px; flex: none; }
  .contact__dot {
    width: 12px; height: 12px; margin: 0 2px;
    border-radius: 50%;
    background: var(--ink-soft);
    flex: none;
  }
</style>
</head>
<body>
<main class="canvas">
  <section class="card front" aria-label="Card front">
    <span class="corner corner--tl"></span>
    <span class="corner corner--bl"></span>
    <span class="corner corner--tr"></span>
    <span class="corner corner--br"></span>
    <div class="front-mark">
      <span class="front-mark__dot"></span>
      <div class="wordmark">
        <span class="wordmark__name">BRENWAY</span>
        <span class="wordmark__sub">PRODUCTIONS</span>
      </div>
    </div>
  </section>

  <section class="card back" aria-label="Card back">
    <div class="back__brand">
      <div class="wordmark">
        <span class="wordmark__name">BRENWAY</span>
        <span class="wordmark__sub">PRODUCTIONS</span>
      </div>
    </div>
    <div class="back__divider"></div>
    <div class="back__details">
      <p class="person__name">DARA BRENWAY</p>
      <p class="person__role">Photographer</p>
      <ul class="contact">
        <li class="contact__item">
          <svg class="contact__icon" viewBox="0 0 24 24" aria-hidden="true"><path fill="#333" d="M6.6 10.8a15.1 15.1 0 0 0 6.6 6.6l2.2-2.2a1 1 0 0 1 1-.25 11.4 11.4 0 0 0 3.6.57 1 1 0 0 1 1 1V20a1 1 0 0 1-1 1A17 17 0 0 1 3 4a1 1 0 0 1 1-1h3.5a1 1 0 0 1 1 1c0 1.25.2 2.45.57 3.57a1 1 0 0 1-.25 1z"/></svg>
          <span>580-331-7264</span>
        </li>
        <li class="contact__item">
          <svg class="contact__icon" viewBox="0 0 24 24" aria-hidden="true"><rect x="2.5" y="5" width="19" height="14" fill="none" stroke="#333" stroke-width="2"/><path d="M2.5 5.5l9.5 7 9.5-7" fill="none" stroke="#333" stroke-width="2"/></svg>
          <span>dara@brenwayproductions.ca</span>
        </li>
        <li class="contact__item">
          <span class="contact__dot"></span>
          <span>dara_brenway</span>
        </li>
      </ul>
    </div>
  </section>
</main>
</body>
</html>
```